【ヘッダー画像(1600 x 600px程度) ×1点】
「グローバルネットワーク」とネット検索すると出てくるような、海外と日本とを線で繋ぐイメージが良いです。
但し、サイトコンセプトが「アジア地域の部品メーカーを紹介するインデックスサイト」ということもあり、世界全体ではなくアジア(特に中国の深センや香港、台湾)と日本とのネットワークに焦点を当てたもの(※)を希望致します。

※弊社が誇るコネクション数(100社以上)を視覚的にアピールできるようなものであれば尚良いと考えています。

【メニュー画像(570 x 375px程度) ×4点】
→これについては指定したいイメージが特になく、コンペ形式で提案してもらった中から良い物があれば、と思っています。

①会社概要・対応方針
②取扱いメーカー
③ニュース/読み物
④問い合わせ】

■画像サイズについて
現在サイトに仮置きしている画像サイズが上記で記載しているものとなるのですが、
特にこのサイズに拘りがあるという訳でもなく、少々大きいようにも感じています。
全体のバランスを見ていただいた上で良いご提案をいただけましたら大変幸いです。
サイト名:ハルカ部品navi
サイト:https://www.haruka-buhin-navi.jp/
• 1600 x 600pxのヘッダー用画像1点、570 x 375pxのメニュー用バナー画像4点
緑系、青系、水色系
• 高解像度JPG (.jpg)
• イラストレーター形式 (.ai)
• PNG形式 (.png)
ヘッダー/バナーのどちらか片方ではなく、全て合わせて5点の画像作成依頼となります。
よろしくお願い致します。

どちらも青を基調としながらも、明るくグローバルな雰囲気や統一感が感じられるデザインで、イメージしていた雰囲気に合っていたことから選ばせていただきました。

この度は良いご提案をいただき誠にありがとうございました。
修正のお願いにも迅速かつご丁寧に対応いただき大変助かりました。
また次のご縁があった際にはどうぞよろしくお願い致します。

```html
<!DOCTYPE html>
<html lang="ja">
<head>
<meta charset="utf-8">
<title>ハルカ部品navi</title>
<link href="https://fonts.googleapis.com/css2?family=Noto+Sans+JP:wght@400;500;700&family=Montserrat:wght@600;800&display=swap" rel="stylesheet">
<style>
:root{
  --ink:#2a3440;
  --navy:#1f4f7a;
  --blue:#2f7fc0;
  --accent:#3a8ed0;
  --teal:#3f8a9c;
  --teal-dark:#2f7487;
  --mist:#eef3f6;
  --line:#d9e1e7;
  --white:#ffffff;
}
*{margin:0;padding:0;box-sizing:border-box}
html,body{width:824px;height:1200px;overflow:hidden;background:var(--white)}
body{font-family:"Noto Sans JP",sans-serif;color:var(--ink);position:relative}
.topline{height:24px;padding:7px 40px 0;font-size:9px;line-height:1;color:#5b6670;letter-spacing:.05em}
.site-header{height:78px;display:flex;justify-content:space-between;align-items:center;padding:0 48px 0 68px}
.brand{display:flex;align-items:center;gap:9px}
.brand-dot{width:24px;height:24px;border-radius:50%;background:var(--accent)}
.brand-name{font-size:26px;font-weight:700;color:var(--navy);letter-spacing:.02em;line-height:1}
.contact-box{text-align:right;line-height:1.2}
.contact-box .company{font-size:10px;color:#444}
.contact-box .tel{font-size:21px;font-weight:700;color:var(--navy);letter-spacing:.02em}
.contact-box .hours{font-size:10px;color:#444}
.global-nav{height:49px;display:flex;align-items:stretch;padding:0 70px 0 68px;border-top:1px solid var(--line);border-bottom:1px solid var(--line)}
.global-nav a{display:flex;align-items:center;justify-content:center;width:110px;font-size:10px;color:#556;text-decoration:none;border-right:1px solid var(--line)}
.global-nav a:first-child{border-left:1px solid var(--line)}
.global-nav a.current{background:#e7ebee;color:var(--navy)}
.global-nav .nav-cta{margin-left:auto;align-self:center;width:100px;height:32px;border:none;background:var(--blue);color:var(--white);border-radius:2px}
.global-nav .nav-cta:first-child{border-left:none}
.hero{position:relative;height:330px;overflow:hidden;background:linear-gradient(115deg,#1f5c82 0%,#3f8fb8 38%,#9fd2e4 62%,#4a8fb0 80%,#1d5275 100%)}
.hero .city{position:absolute;left:0;right:0;bottom:0;height:190px;background:linear-gradient(180deg,rgba(18,62,92,0) 0%,rgba(18,62,92,.6) 100%)}
.hero .network{position:absolute;left:0;top:0;width:824px;height:330px}
.hero .word{position:absolute;left:300px;top:170px;font-family:"Montserrat",sans-serif;font-weight:800;font-size:150px;line-height:1;letter-spacing:.04em;color:rgba(255,255,255,.2);white-space:nowrap}
.hero .tagline{position:absolute;left:0;right:0;top:272px;height:38px;display:flex;align-items:center;justify-content:center;background:rgba(255,255,255,.18);color:var(--white);font-size:16px;font-weight:500;letter-spacing:.22em}
.hero .wedge{position:absolute;left:0;bottom:0;width:100%;height:60px}
.menu-area{background:var(--mist);height:180px;position:relative}
.menu-cards{position:absolute;left:41px;top:-30px;display:flex;gap:12px}
.menu-card{width:239px;height:160px;background:linear-gradient(135deg,#5f9fb6 0%,#3f7f98 100%);color:var(--white);display:flex;flex-direction:column;align-items:center;justify-content:center;gap:6px;text-decoration:none}
.menu-card:nth-child(2){background:linear-gradient(135deg,#6aa7c4 0%,#356f90 100%)}
.menu-card:nth-child(3){background:linear-gradient(135deg,#8cbfd0 0%,#3d7c93 100%)}
.menu-card .label{font-size:11px;font-weight:500;letter-spacing:.08em}
.menu-card .sub{font-family:"Montserrat",sans-serif;font-size:5px;letter-spacing:.2em;opacity:.85}
.contact-section{position:absolute;left:0;top:797px;width:824px;height:220px;background:linear-gradient(180deg,var(--teal) 0%,var(--teal-dark) 100%);color:var(--white);text-align:center;padding-top:50px}
.contact-section h2{font-size:11px;font-weight:500;letter-spacing:.2em}
.contact-section .en{font-family:"Montserrat",sans-serif;font-size:5px;letter-spacing:.25em;opacity:.8;margin-top:4px}
.contact-section p{font-size:9.5px;line-height:2.8;letter-spacing:.22em;margin-top:18px}
.contact-section .btn{display:inline-block;margin-top:14px;width:94px;height:22px;line-height:20px;border:1px solid rgba(255,255,255,.8);font-family:"Montserrat",sans-serif;font-size:5px;letter-spacing:.2em;color:var(--white);text-decoration:none}
</style>
</head>
<body>
<div class="topline">日本メーカーとアジアの部品メーカーを繋ぐ信頼の窓口</div>
<header class="site-header">
  <div class="brand"><span class="brand-dot"></span><span class="brand-name">ハルカ部品navi</span></div>
  <div class="contact-box">
    <div class="company">東邦リンク株式会社</div>
    <div class="tel">03-4821-7730</div>
    <div class="hours">9:00-18:00（月-金）</div>
  </div>
</header>
<nav class="global-nav">
  <a class="current" href="#">ホーム</a>
  <a href="#">会社概要・対応方針</a>
  <a href="#">取扱いメーカー</a>
  <a href="#">ニュース/読み物</a>
  <a class="nav-cta" href="#">お問い合わせ</a>
</nav>
<section class="hero" role="img" aria-label="深セン・香港・台湾などアジアの都市と日本を光の線で結ぶ、100社以上の繋がりを表す青いビル群の写真">
  <div class="city"></div>
  <svg class="network" viewBox="0 0 824 330" aria-hidden="true">
    <g stroke="#ffffff" stroke-opacity=".45" stroke-width=".8" fill="none">
      <path d="M640 90 Q420 20 150 120"/>
      <path d="M640 90 Q430 60 110 170"/>
      <path d="M640 90 Q450 90 180 200"/>
      <path d="M640 90 Q470 130 240 150"/>
      <path d="M640 90 Q500 160 300 230"/>
      <path d="M640 90 Q520 40 380 110"/>
      <path d="M640 90 Q560 150 460 230"/>
      <path d="M640 90 Q700 140 720 240"/>
      <path d="M640 90 Q720 60 790 130"/>
      <path d="M640 90 Q600 10 520 60"/>
      <path d="M640 90 Q380 0 60 90"/>
      <path d="M640 90 Q400 120 70 240"/>
    </g>
    <g stroke="#ffffff" stroke-opacity=".25" stroke-width=".6">
      <line x1="150" y1="120" x2="110" y2="170"/>
      <line x1="110" y1="170" x2="180" y2="200"/>
      <line x1="180" y1="200" x2="240" y2="150"/>
      <line x1="240" y1="150" x2="150" y2="120"/>
      <line x1="60" y1="90" x2="150" y2="120"/>
      <line x1="70" y1="240" x2="180" y2="200"/>
      <line x1="300" y1="230" x2="240" y2="150"/>
      <line x1="380" y1="110" x2="240" y2="150"/>
    </g>
    <g fill="#ffffff">
      <circle cx="640" cy="90" r="5"/>
      <circle cx="640" cy="90" r="12" fill-opacity=".2"/>
      <circle cx="150" cy="120" r="3"/><circle cx="110" cy="170" r="3"/>
      <circle cx="180" cy="200" r="3"/><circle cx="240" cy="150" r="3"/>
      <circle cx="300" cy="230" r="2.5"/><circle cx="380" cy="110" r="2.5"/>
      <circle cx="460" cy="230" r="2.5"/><circle cx="720" cy="240" r="2.5"/>
      <circle cx="790" cy="130" r="2.5"/><circle cx="520" cy="60" r="2.5"/>
      <circle cx="60" cy="90" r="2.5"/><circle cx="70" cy="240" r="2.5"/>
    </g>
  </svg>
  <div class="word">CONNECT</div>
  <div class="tagline">日本メーカーとアジアの部品メーカーを繋ぐ信頼の窓口</div>
  <svg class="wedge" viewBox="0 0 824 60" preserveAspectRatio="none" aria-hidden="true"><polygon points="0,60 0,20 824,60" fill="#eef3f6"/></svg>
</section>
<section class="menu-area">
  <div class="menu-cards">
    <a class="menu-card" href="#" role="img" aria-label="会社概要・対応方針の写真"><span class="label">会社概要・対応方針</span><span class="sub">COMPANY</span></a>
    <a class="menu-card" href="#" role="img" aria-label="取扱いメーカーの写真"><span class="label">取扱いメーカー</span><span class="sub">MAKERS</span></a>
    <a class="menu-card" href="#" role="img" aria-label="ニュース/読み物の写真"><span class="label">ニュース/読み物</span><span class="sub">NEWS</span></a>
  </div>
</section>
<section class="contact-section">
  <h2>お問い合わせ</h2>
  <div class="en">CONTACT US</div>
  <p>日本メーカーとアジアの部品メーカーを繋ぐ信頼の窓口です。<br>貴社専用の部品調達、お気軽にお問い合わせください。</p>
  <a class="btn" href="#">CONTACT US</a>
</section>
</body>
</html>
```